Business Card and Letterhead for Juniper Anvil - (Have Logo)

Update 4: Removed company reg no from business card details as it looked a bit out of place. Updated services list.
UPDATE 3
Sorry, I got the address a little bit wrong, have updated it below. Sorry for any inconvenience caused.
UPDATE 2
Finally I have the details for the business cards and letterhead. Submissions already made do not have to be updated unless shortlisted, if all new submissions could include the details for me, Marcus, that would be very much appreciated and help with the final shortlist selection. I intend to share a shortlist of the three best entries with past and existing customers for their feedback and opinions. Thank you all again for your time.
Here are the details.
Marcus Telby
Web Developer
T: 01632 960 418
E: marcus@juniperanvil.example
www.juniperanvil.example
Professional Photography
Web Solutions & E-Commerce
Audio & HD Video Production
Marketing & Promotions
Identity and Branding
Juniper Anvil Ltd
Suite 20938, 3rd Floor
212-224 Orchard Lane
London, N7 9QX
Company Reg. No: 05829147
The order and the layout of the information are of course down to the design, but the company registration number should be smaller and less prominent. The formatting of the telephone and email address using a T: and an E: I am not sure about and again if it is Tel: or Email: or Icons is up to the design.
The Company No. on the letterhead should read (somewhere in small text along the bottom):
Juniper Anvil is a Ltd Company registered in England & Wales, Registration No. 05829147.
The second business card details are
Oliver Brackley
Photographer
T: 01632 960 418
E: oliver@juniperanvil.example
Everything else the same of course.
Thank you again for all the submissions so far.
END OF UPDATE 2
-
UPDATE 1: Please do not alter the logo nor the logo colours. (This was a previous pixel forum project and I am extremely happy with it. The icon can stand alone of course, but I have had to eliminate all entries that have made it black and white, or reversed the icon.) I would like to thank everyone that has participated so far and am very grateful for all your thought and time.
End of Update 1
-
Original Brief:
I have attached the logo vector file.
Following a superb logo from a previous Pixel Forum project I am now looking for a business card design and (although less important) a letterhead as well.
I must admit I tried to do it myself but could only come up with the usual amateur stuff that in comparison to the quality of the logo looked awful.
About Us
Juniper Anvil Ltd will be a new company due to start in January. It is really just me (a web developer) and my friend (a photographer). We will be aiming at the usual small to medium sized businesses in the local area, selling various digital services including photographic services to the public, web hosting and development, commercial photography, modelling services (not us!), full video and film production and possibly a bit of marketing as well. (Really it is anything we can do professionally all lumped together! We met running seperate businesses which have both since closed)
We will not be competing on price. We plan to be expensive but fair. Certainly not the cheapest.
What we are looking for
Business Card
I imagine a double sided business card, which will be used for more than one person. I imagine the front to be the same for everyone and the persons details to be on the back, although this is of course only my thoughts and I am of course completely open to any ideas.
The card could also have a services list or a bit about what we do on it. It might feature the website address, our business address (mail forwarding address) or our registered company number.
Or it might have none of that, we are completely open to any ideas and have no real fixed opinions. I just want it to be really nice :-)
Letterhead (secondary importance)
We will make our decision primarily on the business card, although a mathcing letterhead would be fantastic. Something standardish in format and simple, although again, all ideas are welcomed.
I hope that is enough information but if you have any questions I will answer them as fully and as quickly as possible.
Thank you once again and I really look forward to seeing your ideas and picking a winner.
Marcus T.
Small businesses AND the general public
Film Production

```html
<!DOCTYPE html>
<html lang="en">
<head>
<meta charset="utf-8">
<title>Juniper Anvil – Business Cards and Letterhead</title>
<link href="https://fonts.googleapis.com/css2?family=Open+Sans:wght@300;400;600;700;800&display=swap" rel="stylesheet">
<style>
  :root {
    --red: #b5121b;
    --ink: #3a3a3c;
    --dark: #1e1e1e;
    --white: #ffffff;
    --stage: #ece8e2;
    --tagline: #d9704f;
    --tagline-grey: #8a8a8a;
    --silver: linear-gradient(90deg, #8f8f92 0%, #d9d9db 22%, #f7f7f7 40%, #a9a9ac 60%, #e6e6e8 80%, #9a9a9d 100%);
    --panel: linear-gradient(90deg, #0f0f0f 0%, #2a2a2a 50%, #3c3c3c 100%);
  }
  * { box-sizing: border-box; margin: 0; padding: 0; }
  html, body { width: 1200px; height: 1200px; overflow: hidden; }
  body {
    background: var(--stage);
    font-family: "Open Sans", Arial, sans-serif;
    position: relative;
    color: var(--ink);
  }

  .card, .letterhead {
    position: absolute;
    background: var(--white);
    box-shadow: 0 2px 8px rgba(0,0,0,.18);
    overflow: hidden;
  }
  .band { position: absolute; left: 0; right: 0; }
  .band--red { background: var(--red); }
  .band--silver { background: var(--silver); }

  /* Wordmark */
  .wordmark {
    display: flex; align-items: center; gap: 8px;
    font-weight: 800; color: var(--red);
    text-transform: uppercase; letter-spacing: .02em;
    position: absolute; white-space: nowrap;
  }
  .wordmark__square { background: var(--ink); flex: none; }

  /* Card front */
  .card--front { left: 24px; top: 132px; width: 438px; height: 242px; }
  .card--front .wordmark { left: 0; right: 0; top: 110px; justify-content: center; font-size: 38px; }
  .card--front .wordmark__square { width: 30px; height: 30px; }

  /* Card back */
  .card--back { left: 24px; width: 438px; height: 241px; }
  .card--marcus { top: 388px; }
  .card--oliver { top: 648px; }
  .card--back .wordmark { left: 243px; top: 43px; font-size: 20px; gap: 6px; }
  .card--back .wordmark__square { width: 14px; height: 14px; }
  .person { position: absolute; left: 10px; top: 50px; }
  .person__name { font-size: 26px; font-weight: 700; color: var(--dark); letter-spacing: -.01em; line-height: 1.1; }
  .person__surname { font-weight: 400; color: var(--red); }
  .person__role { font-size: 17px; font-weight: 600; color: var(--dark); margin-top: 2px; }
  .details {
    position: absolute; left: 0; right: 0; top: 116px; height: 102px;
    background: var(--panel); color: var(--white);
  }
  .contact { position: absolute; left: 10px; top: 8px; font-size: 14px; line-height: 20px; }
  .contact b { font-weight: 700; }
  .contact__web { position: absolute; left: 10px; top: 70px; font-size: 14px; }
  .services { position: absolute; left: 244px; top: 6px; font-size: 13.5px; line-height: 17px; list-style: none; }

  /* Letterhead */
  .letterhead { left: 485px; top: 132px; width: 705px; height: 912px; }
  .letterhead .wordmark { left: 14px; top: 58px; font-size: 24px; gap: 6px; }
  .letterhead .wordmark__square { width: 18px; height: 18px; }
  .tagline {
    position: absolute; right: 8px; top: 55px;
    display: grid; grid-template-columns: auto auto; column-gap: 4px; align-items: center;
    color: var(--tagline); line-height: 1;
  }
  .tagline__big { font-size: 30px; font-weight: 300; text-align: right; letter-spacing: -.01em; }
  .tagline__stack { font-size: 13px; line-height: 1; }
  .tagline__stack b { font-weight: 700; display: block; }
  .tagline__stack span { color: var(--tagline-grey); font-weight: 700; font-size: 11px; display: block; }
  .tagline__stack small { font-weight: 400; font-size: 9px; }
  .tagline__stack i { font-style: normal; font-size: 9px; font-weight: 400; display: block; color: var(--tagline); }

  .faint-mark {
    position: absolute; left: 0; right: 0; top: 390px; text-align: center;
    font-size: 62px; font-weight: 800; color: #f8ece8; text-transform: uppercase; letter-spacing: .02em;
  }
  .registration { position: absolute; left: 0; right: 0; top: 811px; text-align: center; font-size: 8px; color: #9a9a9a; }
  .footer-info { position: absolute; left: 17px; top: 872px; color: var(--white); font-size: 9.5px; line-height: 15px; }
  .footer-info b { font-weight: 700; }
</style>
</head>
<body>

<section class="card card--front" aria-label="Business card front">
  <div class="band band--red" style="top:0;height:10px"></div>
  <div class="band band--silver" style="top:10px;height:44px"></div>
  <div class="band band--silver" style="top:186px;height:46px"></div>
  <div class="band band--red" style="top:232px;height:10px"></div>
  <div class="wordmark"><span class="wordmark__square"></span>Juniper Anvil</div>
</section>

<section class="card card--back card--marcus" aria-label="Business card back, Marcus Telby">
  <div class="band band--red" style="top:0;height:10px"></div>
  <div class="band band--silver" style="top:10px;height:14px"></div>
  <div class="wordmark"><span class="wordmark__square"></span>Juniper Anvil</div>
  <div class="person">
    <div class="person__name">Marcus<span class="person__surname">Telby</span></div>
    <div class="person__role">Web Developer</div>
  </div>
  <div class="details">
    <div class="contact"><b>T:</b>&nbsp; 01632 960 418<br><b>E:</b>&nbsp; marcus@juniperanvil.example</div>
    <div class="contact__web">www.juniperanvil.example</div>
    <ul class="services">
      <li>Professional Photography</li>
      <li>Web Solutions &amp; E-Commerce</li>
      <li>Audio &amp; HD Video Production</li>
      <li>Marketing &amp; Promotions</li>
      <li>Identity and Branding</li>
    </ul>
  </div>
  <div class="band band--silver" style="top:218px;height:14px"></div>
  <div class="band band--red" style="top:232px;height:9px"></div>
</section>

<section class="card card--back card--oliver" aria-label="Business card back, Oliver Brackley">
  <div class="band band--red" style="top:0;height:10px"></div>
  <div class="band band--silver" style="top:10px;height:14px"></div>
  <div class="wordmark"><span class="wordmark__square"></span>Juniper Anvil</div>
  <div class="person">
    <div class="person__name">Oliver<span class="person__surname">Brackley</span></div>
    <div class="person__role">Photographer</div>
  </div>
  <div class="details">
    <div class="contact"><b>T:</b>&nbsp; 01632 960 418<br><b>E:</b>&nbsp; oliver@juniperanvil.example</div>
    <div class="contact__web">www.juniperanvil.example</div>
    <ul class="services">
      <li>Professional Photography</li>
      <li>Web Solutions &amp; E-Commerce</li>
      <li>Audio &amp; HD Video Production</li>
      <li>Marketing &amp; Promotions</li>
      <li>Identity and Branding</li>
    </ul>
  </div>
  <div class="band band--silver" style="top:218px;height:14px"></div>
  <div class="band band--red" style="top:232px;height:9px"></div>
</section>

<section class="letterhead" aria-label="Letterhead">
  <div class="band band--red" style="top:0;height:22px"></div>
  <div class="band band--silver" style="top:22px;height:30px"></div>
  <div class="wordmark"><span class="wordmark__square"></span>Juniper Anvil</div>

  <div class="tagline">
    <div class="tagline__big">PROFESSIONAL</div>
    <div class="tagline__stack"><b>PHOTOGRAPHY</b><span>Web Solutions <small>&amp; E-Commerce</small></span></div>
    <div class="tagline__big">AUDIO &amp;</div>
    <div class="tagline__stack"><b>HD VIDEO PRODUCTION</b><span>Marketing <small>&amp; Promotions</small></span></div>
    <div class="tagline__big">IDENTITY</div>
    <div class="tagline__stack"><i>AND</i><b>BRANDING</b></div>
  </div>

  <div class="faint-mark">Juniper Anvil</div>

  <p class="registration">Juniper Anvil is a Ltd Company registered in England &amp; Wales, Registration No. 05829147.</p>

  <div class="band band--silver" style="top:830px;height:29px"></div>
  <div class="band band--red" style="top:859px;height:53px"></div>
  <div class="footer-info">
    Juniper Anvil Ltd&nbsp; Suite 20938, 3rd Floor 212-224 Orchard Lane London, N7 9QX<br>
    <b>T:</b> 01632 960 418&nbsp;&nbsp; <b>www.juniperanvil.example</b>
  </div>
</section>

</body>
</html>
```